City of Brevik Street Banner

Design a street banner (30x60) that highlights the City of Brevik. Must include: The City of Brevik (wording), Train Caboose silhouette, Water Tower, Parks, Illustrate growth. www.townofbrevik.net

Colors

Designer to choose colors to be used in the design.

```html
<!DOCTYPE html>
<html lang="en">
<head>
<meta charset="utf-8">
<title>The City of Brevik – Street Banner</title>
<link rel="stylesheet" href="https://fonts.googleapis.com/css2?family=Playfair+Display:wght@700;800&family=Montserrat:wght@500;600&display=swap">
<style>
  :root {
    --page-bg: #e9e9e9;
    --banner-red: #e84e4f;
    --accent-pink: #f4a19b;
    --seal-ring: #f6c9c4;
    --seal-ink: #7a1f2a;
    --white: #ffffff;
    --sky: #cfdde8;
    --grass: #6f9a45;
    --stone: #dcd0b8;
    --rust: #b8523a;
    --tower: #eef1f3;
    --trees: #6e8a58;
  }
  html, body {
    margin: 0;
    padding: 0;
    width: 1200px;
    height: 1200px;
    overflow: hidden;
    background: var(--page-bg);
  }
  .canvas {
    position: relative;
    width: 1200px;
    height: 1200px;
  }
  .street-banner {
    position: absolute;
    left: 317px;
    top: 40px;
    width: 566px;
    height: 1120px;
    display: block;
    box-shadow: 0 8px 24px rgba(0,0,0,0.18);
  }
  .banner-title {
    font-family: "Playfair Display", Georgia, serif;
    font-weight: 800;
    fill: var(--white);
    text-anchor: middle;
  }
  .banner-url {
    font-family: "Montserrat", Arial, sans-serif;
    font-weight: 600;
    font-size: 25px;
    fill: var(--white);
    text-anchor: middle;
  }
  .seal-name {
    font-family: "Playfair Display", Georgia, serif;
    font-weight: 800;
    font-size: 24px;
    fill: var(--seal-ink);
    text-anchor: middle;
    letter-spacing: 1px;
  }
</style>
</head>
<body>
<main class="canvas">
  <svg class="street-banner" viewBox="0 0 566 1120" xmlns="http://www.w3.org/2000/svg">
    <defs>
      <linearGradient id="welcome-photo-tone" x1="0" y1="0" x2="0" y2="1">
        <stop offset="0" stop-color="var(--sky)"/>
        <stop offset="0.4" stop-color="var(--stone)"/>
        <stop offset="0.75" stop-color="#9aa673"/>
        <stop offset="1" stop-color="var(--grass)"/>
      </linearGradient>
      <linearGradient id="caboose-photo-tone" x1="0" y1="0" x2="0" y2="1">
        <stop offset="0" stop-color="#e3e8ea"/>
        <stop offset="0.2" stop-color="#c86a4e"/>
        <stop offset="0.7" stop-color="var(--rust)"/>
        <stop offset="1" stop-color="#8f8c68"/>
      </linearGradient>
      <linearGradient id="tower-photo-tone" x1="0" y1="0" x2="0" y2="1">
        <stop offset="0" stop-color="var(--trees)"/>
        <stop offset="0.2" stop-color="var(--tower)"/>
        <stop offset="0.7" stop-color="#e2e6e9"/>
        <stop offset="1" stop-color="#5f7a4c"/>
      </linearGradient>
    </defs>

    <rect class="banner-field" x="0" y="0" width="566" height="1120" fill="var(--banner-red)"/>

    <!-- Welcome monument and park -->
    <rect class="welcome-photo" x="0" y="0" width="566" height="340"
          fill="url(#welcome-photo-tone)" role="img"
          aria-label="Photo of the stone welcome monument at the town entrance with palm trees and park lawn"/>

    <path class="chevron-accent" d="M0,280 L283,326 L566,280 L566,294 L283,340 L0,294 Z" fill="var(--accent-pink)"/>
    <path class="chevron-field" d="M0,294 L283,340 L566,294 L566,1120 L0,1120 Z" fill="var(--banner-red)"/>

    <g class="town-seal">
      <circle cx="287" cy="293" r="74" fill="var(--seal-ring)"/>
      <circle cx="287" cy="293" r="64" fill="var(--white)"/>
      <text class="seal-name" x="287" y="301">BREVIK</text>
    </g>

    <text class="banner-title" x="283" y="487" font-size="100">THE</text>
    <text class="banner-title" x="283" y="583" font-size="104">CITY OF</text>
    <text class="banner-title" x="283" y="721" font-size="130" textLength="480" lengthAdjust="spacingAndGlyphs">BREVIK</text>

    <line class="title-rule" x1="123" y1="749" x2="432" y2="749" stroke="var(--white)" stroke-width="3"/>
    <text class="banner-url" x="283" y="794">www.townofbrevik.net</text>

    <!-- Caboose and water tower -->
    <polygon class="caboose-photo" points="36,802 306,855 405,1088 36,1088"
             fill="url(#caboose-photo-tone)" role="img"
             aria-label="Photo of the restored red railway caboose with wooden steps"/>
    <polygon class="tower-photo" points="306,855 531,784 531,1088 405,1088"
             fill="url(#tower-photo-tone)" role="img"
             aria-label="Photo of the white town water tower above growing neighbourhoods"/>
    <line class="photo-divider" x1="306" y1="855" x2="405" y2="1088" stroke="var(--accent-pink)" stroke-width="4"/>

    <rect class="bottom-accent" x="36" y="1088" width="495" height="6" fill="var(--accent-pink)"/>
  </svg>
</main>
</body>
</html>
```